Current Employment Opportunities Email Template

We would like to redesign our internal job listing email template we send out each month. The email service we use is MailChimp and would like the template to be easy to edit when updating job postings. I attached an example below.

Font styles to use
Sans Serif

Colors

Designer to choose colors to be used in the design.

```html
<!DOCTYPE html>
<html lang="en">
<head>
<meta charset="utf-8">
<title>Current Opportunities – Palisade Services</title>
<link rel="stylesheet" href="https://fonts.googleapis.com/css2?family=PT+Sans:wght@400;700&display=swap">
<style>
  :root {
    --teal: #559a98;
    --ink: #333639;
    --black: #111111;
    --muted: #707070;
    --soft: #a6a6a6;
    --panel: #ececee;
    --rule: #e2e2e4;
    --button: #a9a9aa;
    --white: #ffffff;
  }
  * { box-sizing: border-box; margin: 0; padding: 0; }
  html, body {
    width: 789px; height: 1200px; overflow: hidden;
    background: var(--white);
    font-family: "PT Sans", Arial, sans-serif;
  }
  .email { position: relative; width: 789px; height: 1200px; }

  .brand-header {
    height: 97px; margin: 0 10px;
    border-bottom: 2px solid var(--rule);
    display: flex; justify-content: center; align-items: center;
  }
  .brand-name {
    font-size: 26px; font-weight: 700; color: var(--ink);
    letter-spacing: 1px; line-height: 1;
  }

  .intro { text-align: center; padding-top: 37px; }
  .intro-title {
    font-size: 36px; font-weight: 400; color: var(--teal);
    letter-spacing: 0.5px; line-height: 44px;
  }
  .intro-subtitle {
    margin-top: 12px;
    font-size: 21px; font-weight: 400; color: var(--muted); line-height: 31px;
  }
  .intro-copy {
    width: 632px; margin: 12px auto 0;
    font-size: 15px; color: var(--muted); line-height: 26px;
    hyphens: auto;
  }

  .section-band {
    position: absolute; top: 391px; left: 0; width: 789px; height: 50px;
    background: var(--teal); color: var(--white);
    font-size: 21px; font-weight: 700;
    display: flex; align-items: center; justify-content: center;
  }

  .listings {
    position: absolute; top: 441px; left: 0; width: 789px; height: 686px;
    background: var(--panel);
  }
  .job { position: absolute; left: 95px; width: 576px; height: 140px; }
  .job-divider { position: absolute; left: 95px; width: 576px; height: 2px; background: var(--rule); }
  .job-city {
    position: absolute; left: 1px; top: 0;
    font-size: 28px; font-weight: 700; color: var(--teal); line-height: 34px;
  }
  .job-more {
    position: absolute; left: 15px; top: 100px;
    font-size: 13px; line-height: 16px; color: rgba(255,255,255,0.8);
    text-decoration: none;
  }
  .job-detail { position: absolute; left: 247px; top: 5px; width: 340px; }
  .job-title { font-size: 17px; font-weight: 700; color: var(--ink); line-height: 22px; }
  .job-location { margin-top: 4px; font-size: 14px; color: var(--teal); line-height: 20px; }
  .job-summary { margin-top: 4px; font-size: 14px; color: var(--black); line-height: 20px; }
  .job-button {
    display: inline-block; margin-top: 15px; margin-left: -2px;
    width: 230px; height: 34px; line-height: 34px; padding-left: 10px;
    background: var(--button); color: var(--white);
    font-size: 14px; text-decoration: none;
  }

  .footer {
    position: absolute; top: 1127px; left: 0; width: 789px; height: 73px;
  }
  .footer-note {
    position: absolute; left: 57px; top: 27px;
    font-size: 12px; color: var(--soft);
  }
  .footer-note strong { color: var(--ink); font-weight: 400; }
  .social { position: absolute; left: 609px; top: 29px; display: flex; gap: 16px; }
  .social svg { display: block; }
</style>
</head>
<body>
<main class="email">
  <header class="brand-header">
    <span class="brand-name">PALISADE SERVICES INC.</span>
  </header>

  <section class="intro">
    <h1 class="intro-title">TODAY'S TALENT OPPORTUNITIES</h1>
    <h2 class="intro-subtitle">want to be a part of the most efficient<br>and elite team in the industry?</h2>
    <p class="intro-copy">we've got a list of opportunities here at Palisade that we've love for you to strive for! These open&shy;ings allow you to fully utilize your strength, walk alongside us as we grow exponetially farther than we could ever dream, and leverage your sucess to climb your way up the ladder of profeesional growth and leadership within our organization!</p>
  </section>

  <div class="section-band">Current Opportunities</div>

  <section class="listings">
    <article class="job" style="top:35px">
      <div class="job-city">Dallas</div>
      <a class="job-more" href="#">Read more</a>
      <div class="job-detail">
        <h3 class="job-title">LEAD RESTORATION TECHNICIAN</h3>
        <p class="job-location">Dallas, Tx</p>
        <p class="job-summary">Restoration Technician in the Dallas/Ft. Worth Area</p>
        <a class="job-button" href="#">Learn for About this Opportunity</a>
      </div>
    </article>
    <div class="job-divider" style="top:177px"></div>

    <article class="job" style="top:212px">
      <div class="job-city">Dallas</div>
      <a class="job-more" href="#">Read more</a>
      <div class="job-detail">
        <h3 class="job-title">LEAD RESTORATION TECHNICIAN</h3>
        <p class="job-location">Dallas, Tx</p>
        <p class="job-summary">Restoration Technician in the Dallas/Ft. Worth Area</p>
        <a class="job-button" href="#">Learn for About this Opportunity</a>
      </div>
    </article>
    <div class="job-divider" style="top:353px"></div>

    <article class="job" style="top:374px">
      <div class="job-city">Dallas</div>
      <a class="job-more" href="#">Read more</a>
      <div class="job-detail">
        <h3 class="job-title">LEAD RESTORATION TECHNICIAN</h3>
        <p class="job-location">Dallas, Tx</p>
        <p class="job-summary">Restoration Technician in the Dallas/Ft. Worth Area</p>
        <a class="job-button" href="#">Learn for About this Opportunity</a>
      </div>
    </article>
    <div class="job-divider" style="top:516px"></div>

    <article class="job" style="top:535px">
      <div class="job-city">Dallas</div>
      <a class="job-more" href="#">Read more</a>
      <div class="job-detail">
        <h3 class="job-title">LEAD RESTORATION TECHNICIAN</h3>
        <p class="job-location">Dallas, Tx</p>
        <p class="job-summary">Restoration Technician in the Dallas/Ft. Worth Area</p>
        <a class="job-button" href="#">Learn for About this Opportunity</a>
      </div>
    </article>
  </section>

  <footer class="footer">
    <p class="footer-note"><strong>Palisade Services ©</strong> copyright 2018 - Unsubscribe here</p>
    <div class="social" aria-label="Social links">
      <svg width="16" height="16" viewBox="0 0 16 16" aria-hidden="true"><circle cx="8" cy="8" r="7" fill="#b5b5b5"/></svg>
      <svg width="16" height="16" viewBox="0 0 16 16" aria-hidden="true"><circle cx="8" cy="8" r="7" fill="#b5b5b5"/></svg>
      <svg width="16" height="16" viewBox="0 0 16 16" aria-hidden="true"><circle cx="8" cy="8" r="7" fill="#b5b5b5"/></svg>
    </div>
  </footer>
</main>
</body>
</html>
```